KWI Business Card

Please create a creative design for a business card using the new theme from the Logo & website. This company's main focus is food manufacturing building construction. Please integrate the new logo attached.

Please use the following information for the demo card:

Korvel Walls, Inc.
Dana Whitcombe
dwhitcombe@korvelwalls.example
Cell: 312-555-0178
218 Larkmoor Ave
Alderbrook, MN 60418

See pictures and more information on the website.

www.korvelwalls.example

```html
<!DOCTYPE html>
<html lang="en">
<head>
<meta charset="utf-8">
<title>KWI Business Card</title>
<link rel="stylesheet" href="https://fonts.googleapis.com/css2?family=Arimo:wght@400;700&display=swap">
<style>
  :root {
    --bg: #e8e9eb;
    --brand-blue: #1177bf;
    --rule-blue: #a9c8e6;
    --paper: #ffffff;
    --ink: #333333;
    --muted: #444444;
  }
  * { margin: 0; padding: 0; box-sizing: border-box; }
  html, body { width: 1200px; height: 900px; overflow: hidden; }
  body {
    background: var(--bg);
    font-family: "Arimo", sans-serif;
    position: relative;
  }
  .card {
    position: absolute;
    left: 250px;
    width: 700px;
    height: 400px;
    box-shadow: 0 6px 18px rgba(0,0,0,0.12);
    overflow: hidden;
  }
  .card--front { top: 35px; background: var(--brand-blue); }
  .card--back { top: 465px; background: var(--paper); }

  .front-brand {
    position: absolute;
    inset: 0;
    display: flex;
    flex-direction: column;
    align-items: center;
    justify-content: center;
    gap: 10px;
    color: #ffffff;
    font-weight: 700;
  }
  .front-brand__row { display: flex; align-items: center; gap: 14px; }
  .front-brand__mark { width: 26px; height: 26px; background: #ffffff; }
  .front-brand__initials { font-size: 78px; letter-spacing: 4px; line-height: 1; }
  .front-brand__name { font-size: 26px; letter-spacing: 2px; }

  .back-brand {
    position: absolute;
    left: 46px;
    top: 60px;
    color: var(--brand-blue);
    font-weight: 700;
  }
  .back-brand__row { display: flex; align-items: center; gap: 10px; }
  .back-brand__mark { width: 18px; height: 18px; background: var(--brand-blue); }
  .back-brand__initials { font-size: 54px; letter-spacing: 3px; line-height: 1; }
  .back-brand__name { font-size: 18px; letter-spacing: 1px; margin-top: 8px; }

  .person {
    position: absolute;
    right: 36px;
    top: 168px;
    text-align: right;
  }
  .person__name { color: var(--brand-blue); font-weight: 700; font-size: 30px; line-height: 1.05; }
  .person__title { color: var(--muted); font-size: 17px; margin-top: 2px; }

  .divider {
    position: absolute;
    left: 46px;
    right: 36px;
    top: 232px;
    height: 1px;
    background: var(--rule-blue);
  }

  .contact {
    position: absolute;
    left: 46px;
    top: 246px;
    color: var(--ink);
    font-size: 18px;
    line-height: 24px;
    list-style: none;
  }
  .contact li { display: flex; align-items: center; gap: 8px; }
  .contact__icon { width: 14px; height: 14px; flex: none; }
  .contact__plain { padding-left: 22px; }

  .base-band {
    position: absolute;
    left: 0; right: 0; bottom: 0;
    height: 12px;
    background: var(--brand-blue);
  }
</style>
</head>
<body>
  <section class="card card--front">
    <div class="front-brand">
      <div class="front-brand__row">
        <span class="front-brand__initials">KWI</span>
        <span class="front-brand__mark"></span>
      </div>
      <span class="front-brand__name">Korvel Walls, Inc.</span>
    </div>
  </section>

  <section class="card card--back">
    <div class="back-brand">
      <div class="back-brand__row">
        <span class="back-brand__initials">KWI</span>
        <span class="back-brand__mark"></span>
      </div>
      <div class="back-brand__name">Korvel Walls, Inc.</div>
    </div>

    <div class="person">
      <div class="person__name">Dana Whitcombe</div>
      <div class="person__title">Owner/Founder</div>
    </div>

    <div class="divider"></div>

    <ul class="contact">
      <li class="contact__plain">218 Larkmoor Ave</li>
      <li class="contact__plain">Alderbrook, MN 60418</li>
      <li>
        <svg class="contact__icon" viewBox="0 0 14 14" aria-hidden="true">
          <circle cx="7" cy="7" r="7" fill="#1177bf"/>
          <path d="M4.3 3.6l1.4-.3.7 1.8-.9.6a5 5 0 0 0 2.8 2.8l.6-.9 1.8.7-.3 1.4C7.5 9.9 4.1 6.5 4.3 3.6z" fill="#fff"/>
        </svg>
        312-555-0178
      </li>
      <li>
        <svg class="contact__icon" viewBox="0 0 14 14" aria-hidden="true">
          <rect x="0.5" y="2.5" width="13" height="9" fill="#1177bf"/>
          <path d="M1 3l6 4.5L13 3" fill="none" stroke="#fff" stroke-width="1"/>
        </svg>
        dwhitcombe@korvelwalls.example
      </li>
      <li>
        <svg class="contact__icon" viewBox="0 0 14 14" aria-hidden="true">
          <circle cx="7" cy="7" r="6.5" fill="#1177bf"/>
          <ellipse cx="7" cy="7" rx="2.6" ry="6.3" fill="none" stroke="#fff" stroke-width="0.9"/>
          <path d="M0.8 7h12.4" stroke="#fff" stroke-width="0.9"/>
        </svg>
        www.korvelwalls.example
      </li>
    </ul>

    <div class="base-band"></div>
  </section>
</body>
</html>
```